Flyer-Design für psychologisches Coaching  und Taiji
Flyer-Design für psychologisches Coaching und Taiji
Zielgruppe
Seit Januar 2020 habe ich mich selbständig gemacht und biete unter dem Namen 'WANDELRAUM - Mara Brenner, Coaching und Bewegung' Coaching sowie Taiji an. Der Corona-Lockdown hat meinen Geschäftseintritt stark beeinflusst, so dass ich für den Restart einen professionellen Flyer benötige, um mich und mein Angebot bekannt zu machen. Die Flyer werde ich vor meinen Räumen sowie in Geschäften im Umkreis und/oder per Einwurf verteilen.
Meine Zielgruppe sind gesundheitsorientierte Menschen in der zweiten Lebenshälfte, die ihre Balance finden wollen.
Mehr im separaten Dokument, bitte lesen.
Aufgabenstellung
Das Design soll zum Logo und zu meinem angestrebten Image passen. Ich möchte seriös, sympathisch und authentisch rüberkommen. Das psychologische Coaching und Taiji sollen gleichwertig und harmonisch präsentiert werden. Die Texte sollen kurz und prägnant sein. Textvorschläge gebe ich im Briefing und freue mich über neue, aussagefähige Formulierungen.
Mehr im beigefügten Dokument, bitte lesen.

```html
<!DOCTYPE html>
<html lang="de">
<head>
<meta charset="utf-8">
<title>Wandelraum – Flyer</title>
<link rel="stylesheet" href="https://fonts.googleapis.com/css2?family=Cinzel:wght@500&family=Quicksand:wght@400;500;700&family=Open+Sans:wght@400&display=swap">
<style>
  :root{
    --olive:#a89a36;
    --cream:#f8f7f0;
    --paper:#ffffff;
    --bg:#e4e4e4;
    --ink:#3b3a35;
    --row:#efeddc;
    --serif:"Cinzel", serif;
    --sans:"Quicksand", sans-serif;
    --table:"Open Sans", sans-serif;
  }
  *{box-sizing:border-box;margin:0;padding:0}
  html,body{width:1200px;height:1200px;overflow:hidden}
  body{background:var(--bg);position:relative;font-family:var(--sans);color:var(--ink)}
  .panel{position:absolute;top:122px;width:449px;height:956px;background:var(--cream);overflow:hidden}
  .panel--front{left:75px}
  .panel--back{left:673px}

  .brand{position:absolute;top:0;z-index:2;background:var(--paper);display:flex;align-items:center;justify-content:center;gap:10px;color:var(--olive);font-family:var(--sans);font-weight:700;letter-spacing:1px;line-height:1}
  .panel--front .brand{left:121px;width:206px;height:176px;font-size:21px}
  .panel--back .brand{left:135px;width:178px;height:147px;font-size:18px}
  .brand__dot{flex:none;border-radius:50%;background:var(--olive)}
  .panel--front .brand__dot{width:22px;height:22px}
  .panel--back .brand__dot{width:18px;height:18px}

  .scene{position:absolute;inset:0;background:linear-gradient(180deg,#f9f8ef 0%,#f6f4e2 40%,#f4eec9 55%,#f3d9b0 66%,#eeb79f 75%,#e8a99a 81%,#b5a650 87%,#a89a3a 100%)}
  .headline{position:absolute;top:226px;left:0;width:100%;text-align:center;font-family:var(--serif);font-weight:500;font-size:34px;line-height:39px;color:var(--olive);letter-spacing:1px}
  .offer{position:absolute;top:400px;left:0;width:100%;text-align:center;font-weight:700;font-size:18.5px;color:var(--olive)}
  .formats{position:absolute;top:902px;left:0;width:100%;text-align:center;font-weight:700;font-size:14px;letter-spacing:4.2px;color:#fff}

  .content{position:absolute;left:45px;width:362px}
  .title{top:172px;font-weight:700;font-size:18.6px;color:var(--olive);white-space:nowrap}
  .subtitle{font-weight:700;font-size:12.6px;color:var(--olive);white-space:nowrap}
  .lead{font-size:12.6px;line-height:16.1px}
  .label{font-weight:700;font-size:12.6px;color:var(--ink)}
  .dates{border-collapse:collapse;width:359px;font-family:var(--table);font-size:12.3px;color:var(--ink)}
  .dates td{height:16.1px;padding:0 0 0 6px;line-height:16.1px;white-space:nowrap}
  .dates tr:nth-child(odd){background:var(--row)}
  .dates td:nth-child(1){width:98px}
  .dates td:nth-child(2){width:119px}

  .contact-band{position:absolute;left:0;top:836px;width:100%;height:120px;background:var(--olive)}
  .contact{position:absolute;left:36px;top:788px;width:376px;height:168px;background:var(--paper);text-align:center;color:var(--olive)}
  .contact__title{margin-top:22px;font-weight:700;font-size:15px}
  .contact__line{margin-top:10px;font-size:12.4px}
  .contact__grid{margin-top:8px;display:flex;justify-content:center;font-size:12.4px;line-height:18px}
  .contact__col--left{text-align:right;padding-right:9px;border-right:1px solid var(--olive)}
  .contact__col--right{text-align:left;padding-left:9px}
  .contact__web{margin-top:12px;font-weight:700;font-size:14.5px}
</style>
</head>
<body>

<section class="panel panel--front">
  <div class="scene" role="img" aria-label="Aquarellartige Illustration: Person mit ausgebreiteten Armen auf einer Anhöhe vor Sonnenuntergang und Bergen, Vogel am Himmel"></div>
  <div class="brand"><span class="brand__dot"></span><span>WANDELRAUM</span></div>
  <h1 class="headline">ZU SICH SELBST<br>FINDEN UND ZUR<br>RUHE KOMMEN</h1>
  <p class="offer">COACHING, TAIJI, QIGONG, MEDITATION</p>
  <p class="formats">GRUPPENKURSE UND EINZELUNTERRICHT</p>
</section>

<section class="panel panel--back">
  <div class="brand"><span class="brand__dot"></span><span>WANDELRAUM</span></div>

  <h2 class="content title">AKTUELLE TERMINE IM SOMMER 2020</h2>
  <h3 class="content subtitle" style="top:211px">Kostenlose Schnupperstunde Taiji, Qigong und Meditation</h3>
  <p class="content lead" style="top:236px">Eine Schnupperstunde dauert 75 min und beinhaltet einen Mix aus Taiji, Qigong und Meditation. So können Sie es zuerst ausprobieren, bevor Sie in einen laufenden Kurs einsteigen. Bitte seien sie mindestens 10 min vor Beginn der Stunde da, um sich entsprechend einstimmen zu können. Tragen Sie bequeme Sportkleidung und warme Socken oder Taiji-Schuhe. Auch Stoppersocken oder Barfußschuhe sind okay.</p>
  <p class="content label" style="top:368px">Die nächsten kostenlosen Schnupperstunden:</p>
  <table class="content dates" style="top:394px">
    <tr><td>Mittwoch</td><td>01. Juli 2020</td><td>18:30 Uhr bis 19:45 Uhr</td></tr>
    <tr><td>Mittwoch</td><td>08. Juli 2020</td><td>18:30 Uhr bis 19:45 Uhr</td></tr>
    <tr><td>Donnerstag</td><td>16. Juli 2020</td><td>19:45 Uhr bis 21:00 Uhr</td></tr>
    <tr><td>Montag</td><td>20. Juli 2020</td><td>20:00 Uhr bis 21:15 Uhr</td></tr>
    <tr><td>Mittwoch</td><td>29. Juli 2020</td><td>19:00 Uhr bis 20:15 Uhr</td></tr>
    <tr><td>Donnerstag</td><td>06. August 2020</td><td>19:30 Uhr bis 20:45 Uhr</td></tr>
    <tr><td>Montag</td><td>10. August 2020</td><td>20:00 Uhr bis 21:15 Uhr</td></tr>
    <tr><td>Mittwoch</td><td>19. August 2020</td><td>19:00 Uhr bis 20:15 Uhr</td></tr>
    <tr><td>Freitag</td><td>28. August 2020</td><td>19:00 Uhr bis 20:15 Uhr</td></tr>
  </table>

  <h3 class="content subtitle" style="top:576px">Offener Meditationsabend</h3>
  <p class="content lead" style="top:601px">Einmal im Monat lade ich zu einem offenen Meditationsabend ein. Sie sind herzlich willkommen, ganz unabhängig von Ihrer Meditationserfahrung. Ich biete verschiedene Übungen ohne religiöse oder spirituelle Bindung an und freue mich über einen freiwilligen Kostenbeitrag.</p>
  <p class="content label" style="top:699px">Nächste offene Meditationsabende:</p>
  <table class="content dates" style="top:725px">
    <tr><td>Freitag</td><td>24. Juli 2020</td><td>19:00 Uhr bis 20:15 Uhr</td></tr>
    <tr><td>Mittwoch</td><td>26. August 2020</td><td>19:30 Uhr bis 20:45 Uhr</td></tr>
  </table>

  <div class="contact-band"></div>
  <div class="contact">
    <p class="contact__title">KONTAKT:</p>
    <p class="contact__line">Wandelraum - Mara Brenner - Coaching und Bewegung</p>
    <div class="contact__grid">
      <div class="contact__col--left">Lindenweg 7<br>61440 Oberursel</div>
      <div class="contact__col--right">info@wandelraum-coaching.de<br>mobil: 0151 2046 917</div>
    </div>
    <p class="contact__web">www.wandelraum-coaching.de</p>
  </div>
</section>

</body>
</html>
```